Postcard Design

Baxley is a vip taxi and hire car service that specializes in airport to hotel transfers and surrounding suburbs at affordable rates . we offer a personalize service with over 40 years industry experience. we would like to promote a special from melbourne cbd to airport for $65 , our contact number is 0481926370, email primecabride@brisolmail.com , facebook orbit cab and rental car services we plan on distributing these flyers at all major hotels

Industry/Entity Type

Hotel

```html
<!DOCTYPE html>
<html lang="en">
<head>
<meta charset="UTF-8">
<title>Baxley VIP Taxi Postcard</title>
<link rel="stylesheet" href="https://fonts.googleapis.com/css2?family=Roboto+Condensed:wght@400;700&family=Open+Sans:wght@400;600;700&display=swap">
<style>
:root{
  --red:#e8202a;
  --charcoal:#333132;
  --header-grey:#d3d3d3;
  --white:#ffffff;
  --ink:#1f1f1f;
  --rule:#c9c9c9;
  --stage:#e9e9e9;
}
*{box-sizing:border-box;margin:0;padding:0}
html,body{width:920px;height:1200px;overflow:hidden}
body{background:var(--stage);font-family:"Open Sans",sans-serif;position:relative}
.card{position:absolute;width:643px;height:497px;background:var(--white);box-shadow:0 6px 18px rgba(0,0,0,.22);overflow:hidden}
.card--front{left:83px;top:62px}
.card--back{left:161px;top:607px}

/* front */
.front-header{position:absolute;left:0;top:0;width:100%;height:92px;background:var(--header-grey)}
.brand{font-family:"Roboto Condensed",sans-serif;font-weight:700;color:var(--red);letter-spacing:.5px;line-height:1}
.front-header .brand{position:absolute;left:24px;top:18px;font-size:47px}
.front-header .tagline{position:absolute;left:25px;top:66px;font-size:11.5px;color:var(--ink)}
.front-header .service{position:absolute;left:222px;top:32px;font-family:"Roboto Condensed",sans-serif;font-weight:700;font-size:24px;color:var(--red)}
.hero-photo{position:absolute;left:0;top:92px;width:100%;height:280px;
  background:
    linear-gradient(90deg,rgba(255,255,255,.18) 0%,rgba(255,255,255,0) 35%,rgba(0,0,0,0) 65%,rgba(0,0,0,.25) 100%),
    linear-gradient(180deg,#e1e3e5 0%,#c9ccce 38%,#9a9d9f 55%,#4a4b4d 68%,#222224 82%,#171718 100%)}
.front-footer{position:absolute;left:0;top:372px;width:100%;height:125px;background:var(--charcoal)}
.offer-ribbon{position:absolute;left:0;top:351px;width:474px;height:66px}
.offer-ribbon .label{position:absolute;left:18px;top:8px;font-family:"Roboto Condensed",sans-serif;font-weight:700;font-size:12.5px;color:#ffd3d3}
.offer-ribbon .route{position:absolute;left:16px;top:27px;font-family:"Roboto Condensed",sans-serif;font-size:19.5px;color:var(--white)}
.offer-ribbon .price{position:absolute;left:351px;top:12px;font-family:"Open Sans",sans-serif;font-weight:700;font-size:39px;color:var(--white);line-height:1}
.car-shot{position:absolute;border-radius:38% 45% 14% 14%/55% 55% 22% 22%;background:linear-gradient(180deg,#a4a6a8 0%,#66686b 50%,#2b2c2e 100%)}
.front-footer .car-shot{left:25px;top:60px;width:102px;height:46px}
.contact-phone{position:absolute;display:flex;align-items:center;gap:9px;color:var(--white);font-weight:700;white-space:nowrap}
.front-footer .contact-phone{left:146px;top:63px;font-size:20px}
.contact-links{color:var(--white);font-size:10px;white-space:nowrap}
.front-footer .contact-links{position:absolute;right:14px;top:89px;font-family:"Roboto Condensed",sans-serif;font-size:9.5px}

/* back */
.back-header{position:absolute;left:0;top:0;width:372px;height:98px;background:var(--header-grey);text-align:center}
.back-header .brand{margin-top:22px;font-size:38px}
.back-header .service{margin-top:6px;font-family:"Roboto Condensed",sans-serif;font-weight:700;font-size:20px;color:var(--red)}
.back-body{position:absolute;left:0;top:98px;width:372px;height:277px;background:var(--charcoal)}
.features{list-style:none;position:absolute;left:20px;top:27px;width:340px}
.features li{position:relative;padding-left:19px;color:var(--white);font-size:13.3px;line-height:18px;margin-bottom:12px}
.features svg{position:absolute;left:0;top:3px}
.back-body .car-shot{left:25px;top:165px;width:253px;height:103px}
.back-contact{position:absolute;left:0;top:378px;width:372px;height:74px;background:var(--red);text-align:center}
.back-contact .contact-phone{left:0;right:0;justify-content:center;top:8px;font-size:21px}
.back-contact .contact-links{position:absolute;left:0;right:0;top:46px;font-size:9.5px}
.stamp-box{position:absolute;left:547px;top:29px;width:73px;height:51px;border:1px solid var(--rule)}
.address-line{position:absolute;left:415px;width:204px;height:1px;background:var(--rule)}
</style>
</head>
<body>

<section class="card card--front">
  <header class="front-header">
    <div class="brand">BAXLEY</div>
    <div class="tagline">over 40 years industry experience</div>
    <div class="service">VIP TAXI AND HIRE CAR SERVICE</div>
  </header>
  <div class="hero-photo" role="img" aria-label="Photo of a chauffeur holding an umbrella for a passenger stepping out of a black luxury sedan beside a private jet"></div>
  <div class="front-footer">
    <div class="car-shot" role="img" aria-label="Photo of a grey sedan"></div>
    <div class="contact-phone">
      <svg width="30" height="30" viewBox="0 0 30 30" aria-hidden="true">
        <path d="M15 3a12 12 0 1 1-11 7" fill="none" stroke="#fff" stroke-width="2.4"/>
        <path d="M2 6l2.5 5 4.5-3" fill="none" stroke="#fff" stroke-width="2"/>
        <text x="15" y="19" text-anchor="middle" font-family="Open Sans,sans-serif" font-weight="700" font-size="10" fill="#fff">24</text>
      </svg>
      <span>0481926370</span>
    </div>
    <div class="contact-links">primecabride@brisolmail.com &nbsp;|&nbsp; facebook orbit cab and rental car services</div>
  </div>
  <div class="offer-ribbon">
    <svg width="474" height="66" viewBox="0 0 474 66" style="position:absolute;left:0;top:0" aria-hidden="true">
      <polygon points="0,0 446,0 474,66 0,66" fill="var(--red)"/>
    </svg>
    <div class="label">SPECIAL OFFER</div>
    <div class="route">FROM MELBOURNE CBD TO AIRPORT FOR</div>
    <div class="price">$65</div>
  </div>
</section>

<section class="card card--back">
  <header class="back-header">
    <div class="brand">BAXLEY</div>
    <div class="service">VIP TAXI AND HIRE CAR SERVICE</div>
  </header>
  <div class="back-body">
    <ul class="features">
      <li><svg width="11" height="11" viewBox="0 0 11 11" aria-hidden="true"><circle cx="5.5" cy="5.5" r="4.6" fill="none" stroke="var(--red)" stroke-width="1.2"/><path d="M4.5 3.3l2.2 2.2-2.2 2.2" fill="none" stroke="var(--red)" stroke-width="1.2"/></svg>Specializes in airport to hotel transfers and surrounding suburbs at affordable rates.</li>
      <li><svg width="11" height="11" viewBox="0 0 11 11" aria-hidden="true"><circle cx="5.5" cy="5.5" r="4.6" fill="none" stroke="var(--red)" stroke-width="1.2"/><path d="M4.5 3.3l2.2 2.2-2.2 2.2" fill="none" stroke="var(--red)" stroke-width="1.2"/></svg>We offer a personalize service with over 40 years industry experience</li>
    </ul>
    <div class="car-shot" role="img" aria-label="Photo of a grey executive sedan"></div>
  </div>
  <div class="back-contact">
    <div class="contact-phone">
      <svg width="30" height="30" viewBox="0 0 30 30" aria-hidden="true">
        <path d="M15 3a12 12 0 1 1-11 7" fill="none" stroke="#fff" stroke-width="2.4"/>
        <path d="M2 6l2.5 5 4.5-3" fill="none" stroke="#fff" stroke-width="2"/>
        <text x="15" y="19" text-anchor="middle" font-family="Open Sans,sans-serif" font-weight="700" font-size="10" fill="#fff">24</text>
      </svg>
      <span>0481926370</span>
    </div>
    <div class="contact-links">primecabride@brisolmail.com &nbsp;|&nbsp; facebook orbit cab and rental car services</div>
  </div>
  <div class="stamp-box"></div>
  <div class="address-line" style="top:145px"></div>
  <div class="address-line" style="top:171px"></div>
  <div class="address-line" style="top:198px"></div>
  <div class="address-line" style="top:224px"></div>
  <div class="address-line" style="top:251px"></div>
</section>

</body>
</html>
```